Business Cards for Quenlow Massage and Wellness

I worked with designers from Pixel Harbor to make a wonderful logo and now I would like to use it in a business card. I have an intimate but progressive small clinical massage practice with far infrared sauna therapy for detox, vitasuction for pre and post surgery healing and ashiatsu and sports massage. We do lots of different modalities and I would like each therapist to have the same business card with their names on them. I would like to express our professionalism and connection to health.

I am attaching my logo and would like that included in the design. I love blues and greens. I would like something clean but creative, professional yet personality. I love the font copperplate gothic or I suppose whatever matches the logo. I would like to have the following information on the front of the card...

1. Logo

2. Address: Maplegate Square
5817 Tolvey Rd
Richmond, Va 23228
3. Phone: 804 555-0193

4. www.quenlowmassageandwellness.example

5. name of therapist, CMT (for example purposes Corin Battaway, CMT)

6. Optional information for front of card....
Far Infrared Sauna, Neuromuscular Therapy, VitaSuction, Detox Program, Deep Tissue, Swedish, Ashiatsu, Craniosacral Therapy, Reiki, Sports Massage, Couples Massage, Hot Stones, Cold Stones, LED Light Therapy

back of card...

1. Appointment Date/Time

2. Please provide 24 hours notice of cancellations

3. a line or space for appointment times.

```html
<!DOCTYPE html>
<html lang="en">
<head>
<meta charset="utf-8">
<title>Quenlow Massage and Wellness – Business Card</title>
<link href="https://fonts.googleapis.com/css2?family=EB+Garamond:wght@400;500;700&display=swap" rel="stylesheet">
<style>
  :root {
    --page: #e7e4e0;
    --card-white: #ffffff;
    --card-teal: #7cb2a6;
    --ink: #1f1f1f;
    --gold: #a48c5a;
    --teal-ink: #4f9c92;
    --rule: #b9a77f;
    --faint: #ecebe8;
    --faint-teal: #8fbfb3;
    --back-ink: #ffffff;
  }
  * { box-sizing: border-box; margin: 0; padding: 0; }
  html, body {
    width: 1200px; height: 900px; overflow: hidden;
    background: var(--page);
    font-family: "EB Garamond", Georgia, serif;
  }
  .sheet {
    width: 1200px; height: 900px;
    display: flex; flex-direction: column; align-items: center; justify-content: center;
    gap: 36px;
  }
  .card {
    position: relative; overflow: hidden;
    width: 700px; height: 400px;
    box-shadow: 0 6px 18px rgba(0,0,0,.18);
  }

  /* Front */
  .card-front { background: var(--card-white); }
  .front-decor {
    position: absolute; right: -70px; bottom: -90px;
    width: 380px; height: 380px; border-radius: 50%;
    background: var(--faint);
  }
  .brand {
    position: absolute; left: 60px; top: 52px;
    display: flex; align-items: center; gap: 14px;
  }
  .brand-dot {
    width: 40px; height: 40px; border-radius: 50%;
    background: var(--teal-ink);
  }
  .brand-name {
    font-size: 30px; font-weight: 500; color: var(--gold);
    letter-spacing: 0.04em;
  }
  .contact {
    position: absolute; left: 60px; top: 150px;
    color: var(--ink);
  }
  .therapist {
    font-size: 22px; font-weight: 700; letter-spacing: 0.02em;
    margin-bottom: 12px;
  }
  .address {
    border-left: 2px solid var(--rule);
    padding-left: 14px;
    font-size: 18px; line-height: 1.4;
    margin-bottom: 14px;
  }
  .phone {
    display: flex; align-items: center; gap: 8px;
    font-size: 18px; margin-bottom: 8px;
  }
  .phone svg { width: 16px; height: 16px; }
  .web { font-size: 18px; color: var(--teal-ink); }

  /* Back */
  .card-back { background: var(--card-teal); color: var(--back-ink); }
  .back-decor {
    position: absolute; left: 50%; top: 50%;
    width: 300px; height: 300px; margin: -150px 0 0 -150px;
    border-radius: 50%; background: var(--faint-teal);
  }
  .appointments {
    position: relative;
    padding: 62px 0 0 0;
    display: flex; flex-direction: column; align-items: center;
  }
  .appt-row {
    display: flex; gap: 40px;
    font-size: 20px; line-height: 2;
  }
  .blank { display: inline-block; border-bottom: 1px solid var(--back-ink); height: 1em; vertical-align: baseline; }
  .b-short { width: 26px; }
  .b-year { width: 44px; }
  .b-time { width: 44px; }
  .notice {
    position: relative; text-align: center;
    font-size: 15px; margin-top: 26px;
  }
</style>
</head>
<body>
<main class="sheet">
  <section class="card card-front" aria-label="Business card front">
    <div class="front-decor"></div>
    <div class="brand">
      <span class="brand-dot"></span>
      <span class="brand-name">Quenlow Massage and Wellness</span>
    </div>
    <div class="contact">
      <p class="therapist">CORIN BATTAWAY, CMT</p>
      <p class="address">Maplegate Square<br>5817 Tolvey Rd<br>Richmond, Va 23228</p>
      <p class="phone">
        <svg viewBox="0 0 24 24" aria-hidden="true"><path fill="#a48c5a" d="M6.6 10.8a15.1 15.1 0 0 0 6.6 6.6l2.2-2.2c.3-.3.7-.4 1-.2 1.1.4 2.3.6 3.6.6.6 0 1 .4 1 1V20c0 .6-.4 1-1 1A17 17 0 0 1 3 4c0-.6.4-1 1-1h3.5c.6 0 1 .4 1 1 0 1.3.2 2.5.6 3.6.1.3 0 .7-.2 1z"/></svg>
        804 555-0193
      </p>
      <p class="web">www.quenlowmassageandwellness.example</p>
    </div>
  </section>

  <section class="card card-back" aria-label="Business card back">
    <div class="back-decor"></div>
    <div class="appointments">
      <div class="appt-row"><span>Appointment Date: <span class="blank b-short"></span> / <span class="blank b-short"></span> / <span class="blank b-year"></span></span><span>Time: <span class="blank b-time"></span> AM/PM</span></div>
      <div class="appt-row"><span>Appointment Date: <span class="blank b-short"></span> / <span class="blank b-short"></span> / <span class="blank b-year"></span></span><span>Time: <span class="blank b-time"></span> AM/PM</span></div>
      <div class="appt-row"><span>Appointment Date: <span class="blank b-short"></span> / <span class="blank b-short"></span> / <span class="blank b-year"></span></span><span>Time: <span class="blank b-time"></span> AM/PM</span></div>
      <div class="appt-row"><span>Appointment Date: <span class="blank b-short"></span> / <span class="blank b-short"></span> / <span class="blank b-year"></span></span><span>Time: <span class="blank b-time"></span> AM/PM</span></div>
      <div class="appt-row"><span>Appointment Date: <span class="blank b-short"></span> / <span class="blank b-short"></span> / <span class="blank b-year"></span></span><span>Time: <span class="blank b-time"></span> AM/PM</span></div>
    </div>
    <p class="notice">*Please provide 24 hours notice of cancellations</p>
  </section>
</main>
</body>
</html>
```